Dance school needs a poster to promote our annual concert

I have a dance school called 'The Marcella Dunwoody Dancers'
See designs from previous years
This year's concert theme is Brant Holloway animation movies
The title of the concert is "glimmeRa"
Dance items will be choreographed to; “Quiet Orchard”, Copper Heron”, “The Nine Lanterns”, “The Fox Regent”, “Temrik”, “Willow & the Warden” & “Pipsqueeve”.
I need a colorful A4 (portrait) poster promoting the concert.

Target Market(s)

Families of students & dance community

Industry/Entity Type

Dance Studio

Font styles to use
Other font styles liked:
• "Mistral" for my my name (see examples supplied)

Colors

Designer to choose colors to be used in the design.

Requirements
Must have
• Must Have:
• - The poster must include the following information:
• 'The Marcella Dunwoody Dancers'
• presents
• "glimmeRa"
• (Font for my name is "Mistral")
• Saturday 18th November 2017
• Corbett Hall,
• Halverd Grammar Elmstead.

```html
<!DOCTYPE html>
<html lang="en">
<head>
<meta charset="utf-8">
<title>glimmeRa – The Marcella Dunwoody Dancers</title>
<link href="https://fonts.googleapis.com/css2?family=Caveat:wght@500&family=Great+Vibes&family=Ubuntu:wght@400;500&display=swap" rel="stylesheet">
<style>
  :root {
    --night: #0a1446;
    --deep: #0e2c74;
    --glow: #2f9be0;
    --ice: #8fe4ff;
    --violet: #6a4fd0;
    --magenta: #b05ad8;
    --teal: #26c2d8;
    --castle: #1b3a8c;
    --foliage: #142567;
    --ink-white: #ffffff;
    --footer: #0b1546;
  }
  html, body {
    margin: 0;
    padding: 0;
    width: 849px;
    height: 1200px;
    overflow: hidden;
    background: var(--night);
  }
  .poster {
    position: relative;
    width: 849px;
    height: 1200px;
    overflow: hidden;
    color: var(--ink-white);
    font-family: "Ubuntu", sans-serif;
    background:
      radial-gradient(ellipse 50% 38% at 50% 42%, rgba(143,228,255,0.75), rgba(47,155,224,0.35) 55%, transparent 80%),
      radial-gradient(ellipse 28% 20% at 84% 9%, rgba(143,228,255,0.7), transparent 75%),
      radial-gradient(ellipse 22% 18% at 12% 62%, rgba(106,79,208,0.45), transparent 75%),
      radial-gradient(ellipse 24% 18% at 90% 66%, rgba(176,90,216,0.35), transparent 75%),
      radial-gradient(ellipse 30% 14% at 20% 12%, rgba(38,194,216,0.25), transparent 75%),
      linear-gradient(180deg, #0a2462 0%, var(--deep) 22%, #1c5cb0 45%, #1a4ea6 62%, #15307e 80%, var(--night) 100%);
  }
  .fairy-art {
    position: absolute;
    left: 660px;
    top: 54px;
    width: 132px;
    height: 186px;
    border-radius: 50%;
    background: radial-gradient(ellipse at center, rgba(200,244,255,0.85), rgba(143,228,255,0.35) 55%, transparent 78%);
  }
  .castle-art {
    position: absolute;
    left: 313px;
    top: 540px;
    width: 400px;
    height: 500px;
    border-radius: 40% 40% 0 0;
    background: linear-gradient(180deg, rgba(27,58,140,0) 0%, rgba(27,58,140,0.75) 30%, var(--castle) 70%, rgba(20,37,103,0.9) 100%);
  }
  .garden-art {
    position: absolute;
    left: 0;
    top: 650px;
    width: 849px;
    height: 430px;
    background:
      radial-gradient(ellipse 18% 30% at 8% 70%, rgba(106,79,208,0.55), transparent 75%),
      radial-gradient(ellipse 18% 30% at 92% 72%, rgba(176,90,216,0.45), transparent 75%),
      radial-gradient(ellipse 14% 20% at 70% 80%, rgba(38,194,216,0.35), transparent 75%),
      linear-gradient(180deg, rgba(20,37,103,0) 0%, rgba(20,37,103,0.55) 45%, var(--foliage) 82%, var(--footer) 100%);
  }
  .footer-band {
    position: absolute;
    left: 0;
    bottom: 0;
    width: 849px;
    height: 130px;
    background: var(--footer);
  }
  .brand-mark {
    position: absolute;
    top: 84px;
    left: 0;
    width: 849px;
    display: flex;
    justify-content: center;
    align-items: center;
    gap: 12px;
    font-weight: 500;
    font-size: 54px;
    letter-spacing: 3px;
  }
  .brand-mark .dot {
    width: 14px;
    height: 14px;
    border-radius: 50%;
    background: var(--ink-white);
  }
  .school-name {
    position: absolute;
    top: 180px;
    width: 849px;
    margin: 0;
    text-align: center;
    font-family: "Caveat", cursive;
    font-weight: 500;
    font-size: 48px;
  }
  .presents {
    position: absolute;
    top: 272px;
    width: 849px;
    margin: 0;
    text-align: center;
    font-size: 42px;
  }
  .show-title {
    position: absolute;
    top: 395px;
    width: 849px;
    margin: 0;
    text-align: center;
    font-family: "Great Vibes", cursive;
    font-weight: 400;
    font-size: 190px;
    line-height: 1;
    text-shadow: 0 0 20px rgba(143,228,255,0.6);
  }
  .details {
    position: absolute;
    top: 660px;
    width: 849px;
    text-align: center;
    font-weight: 500;
    text-shadow: 0 2px 8px rgba(5,15,50,0.7);
  }
  .details p { margin: 0; line-height: 1.1; }
  .details .day { font-size: 41px; }
  .details .date { font-size: 51px; }
  .details .date sup { font-size: 20px; }
  .details .venue { font-size: 52px; margin-top: 20px; }
  .details .campus { font-size: 40px; }
  .website {
    position: absolute;
    top: 1122px;
    width: 849px;
    margin: 0;
    text-align: center;
    font-size: 40px;
  }
</style>
</head>
<body>
  <main class="poster">
    <div class="fairy-art" role="img" aria-label="Glowing fairy illustration"></div>
    <div class="castle-art" role="img" aria-label="Silhouetted fairytale castle"></div>
    <div class="garden-art" role="img" aria-label="Enchanted garden foliage with glowing fireflies"></div>
    <div class="footer-band"></div>

    <div class="brand-mark"><span class="dot"></span><span>MDD</span></div>
    <h2 class="school-name">The Marcella Dunwoody Dancers</h2>
    <p class="presents">Presents</p>
    <h1 class="show-title">glimmeRa</h1>

    <section class="details">
      <p class="day">Saturday</p>
      <p class="date">18<sup>th</sup> November 2017</p>
      <p class="venue">Corbett Hall,</p>
      <p class="campus">Halverd Grammar Elmstead</p>
    </section>

    <p class="website">dunwoodydancers.com.au</p>
  </main>
</body>
</html>
```